Design Business Card CORAL TIDE MOWING

We have attached a copy of our Logo, we like a business card designed with logo and mobile phone number on one side that stands out maybe gloss and on the other side it can have the services we do small picture of our logo name number, I have attached an idea to this that I have seen online, this is a business owned by a woman so we like pinks black and navy
Our logo is attached in pdf
Target Market(s)
Home owners that need lawns mowed
Industry/Entity Type
Lawns and gardens
Contact Information for Business Card
Logo business Owner name Dorinda Pask mobile number 0417296054
Font styles to use
Look and feel
Each slider illustrates characteristics of the customer's brand and the style your logo design should communicate.

```html
<!DOCTYPE html>
<html lang="en">
<head>
<meta charset="utf-8">
<title>Coral Tide Mowing – Business Card</title>
<link href="https://fonts.googleapis.com/css2?family=Montserrat:wght@500;600;800&family=Oswald:wght@500&display=swap" rel="stylesheet">
<style>
  :root {
    --pink: #e0329a;
    --pink-deep: #d12586;
    --pink-light: #ea5fb3;
    --ink: #2b2b2b;
    --grey: #3d3d3d;
    --green: #3fbf4a;
    --white: #ffffff;
    --stage: #3a3a3c;
  }
  * { box-sizing: border-box; margin: 0; padding: 0; }
  html, body { width: 1200px; height: 1200px; overflow: hidden; }
  body {
    background: var(--stage);
    display: flex;
    flex-direction: column;
    align-items: center;
    justify-content: center;
    gap: 60px;
    font-family: "Montserrat", sans-serif;
  }
  .card {
    position: relative;
    width: 900px;
    height: 514px;
    border-radius: 34px;
    overflow: hidden;
  }
  /* Front */
  .card-front { background: var(--white); }
  .front-brand {
    position: absolute;
    top: 110px;
    right: 70px;
    display: flex;
    align-items: center;
    gap: 16px;
  }
  .brand-dot {
    width: 58px; height: 58px;
    border-radius: 50%;
    background: var(--pink);
  }
  .brand-name {
    font-weight: 800;
    color: var(--pink);
    font-size: 34px;
    letter-spacing: 1px;
  }
  .contact {
    position: absolute;
    left: 80px;
    top: 168px;
  }
  .contact-name {
    color: var(--pink);
    font-weight: 600;
    font-size: 42px;
    letter-spacing: 1px;
    text-transform: uppercase;
    line-height: 1;
  }
  .contact-role {
    color: var(--grey);
    font-weight: 500;
    font-size: 22px;
    margin-top: 6px;
    margin-left: 34px;
    text-transform: uppercase;
  }
  .contact-phone {
    display: flex;
    align-items: center;
    gap: 12px;
    margin-top: 18px;
    margin-left: 44px;
    color: var(--ink);
    font-weight: 600;
    font-size: 36px;
    letter-spacing: 1px;
  }
  .services-band {
    position: absolute;
    left: 0; right: 0;
    bottom: 88px;
    height: 68px;
    background: linear-gradient(90deg, var(--pink-deep), var(--pink-light) 50%, var(--pink-deep));
    display: flex;
    align-items: center;
    justify-content: center;
    gap: 12px;
    font-family: "Oswald", sans-serif;
    font-weight: 500;
    font-size: 25px;
    color: var(--white);
    letter-spacing: 0.5px;
  }
  .services-band .sep {
    width: 9px; height: 9px;
    border-radius: 50%;
    background: var(--green);
  }
  /* Back */
  .card-back {
    background: linear-gradient(135deg, var(--pink-light), var(--pink) 45%, var(--pink-deep));
    display: flex;
    align-items: center;
    justify-content: center;
    gap: 22px;
  }
  .card-back .brand-dot {
    width: 90px; height: 90px;
    background: var(--ink);
  }
  .card-back .brand-name {
    color: var(--white);
    font-size: 54px;
  }
</style>
</head>
<body>
  <section class="card card-front">
    <div class="front-brand">
      <span class="brand-dot"></span>
      <span class="brand-name">CORAL TIDE MOWING</span>
    </div>
    <div class="contact">
      <p class="contact-name">Dorinda Pask</p>
      <p class="contact-role">Owner</p>
      <p class="contact-phone">
        <svg width="34" height="34" viewBox="0 0 34 34" aria-hidden="true">
          <circle cx="17" cy="17" r="17" fill="var(--pink)"/>
          <path d="M12 9c1 0 2 2.5 2.3 3.5.2.8-1.2 1.6-1 2.4.6 2 2.8 4.2 4.8 4.8.8.2 1.6-1.2 2.4-1 1 .3 3.5 1.3 3.5 2.3 0 1.4-1.6 3-3 3-6 0-12-6-12-12 0-1.4 1.6-3 3-3z" fill="var(--white)"/>
        </svg>
        041.729.6054
      </p>
    </div>
    <div class="services-band">
      <span>GARDEN MAINTENANCE</span><span class="sep"></span>
      <span>RUBBISH REMOVAL</span><span class="sep"></span>
      <span>TRIMMING</span><span class="sep"></span>
      <span>WEEDING</span><span class="sep"></span>
      <span>LAWN CARE</span>
    </div>
  </section>

  <section class="card card-back">
    <span class="brand-dot"></span>
    <span class="brand-name">CORAL TIDE MOWING</span>
  </section>
</body>
</html>
```